New Zealand Luggage Importer Needs Business Cards

We need professional, creative and fashionable business cards created.
We are based in New Zealand and import and distribute high-end, quality, fashionable and durable luggage.
We pride ourselves on selling the very best quality luggage, second only to 1 brand (which we won't mention here)...we use the same manufacturer. However, our prices are much more reasonable.
Industry/Entity Type
Business
Contact Information for Business Card
Mark Dunsley
027 512 4068
3/17 Harlow Street, Pinecrest Flats, Auckland, 0614
PO Box 204377, Fernside, Auckland 0731
09-528-3916
sales@brivancases.co.nz / www.brivancases.co.nz

```html
<!DOCTYPE html>
<html lang="en">
<head>
<meta charset="utf-8">
<title>Brivan Cases – Business Cards</title>
<link href="https://fonts.googleapis.com/css2?family=Open+Sans:wght@400;600;700&display=swap" rel="stylesheet">
<style>
  :root{
    --backdrop:#4e5a77;
    --card:#2e3032;
    --panel-dark:#252628;
    --panel-mid:#37383c;
    --strip:#28292b;
    --orange:#eb9d35;
    --teal:#7fb8a8;
    --text:#e8e8e8;
    --rule:#26272a;
  }
  *{box-sizing:border-box;margin:0;padding:0}
  html,body{width:1200px;height:1200px;overflow:hidden}
  body{background:var(--backdrop);font-family:"Open Sans",Arial,sans-serif;position:relative}
  .card{position:absolute;top:250px;width:400px;height:700px;background:var(--card);box-shadow:0 18px 40px rgba(0,0,0,.35)}
  .card--front{left:170px}
  .card--back{left:630px}

  .brand-strip{position:absolute;left:20px;top:80px;width:360px;height:64px;background:var(--strip);display:flex;align-items:center;padding-left:26px}
  .brand-name{color:#fff;font-weight:700;font-size:30px;letter-spacing:3px}

  .contact-panel{position:absolute;left:36px;top:210px;width:344px;height:400px;background:var(--panel-dark)}
  .name-bar{position:absolute;left:70px;top:0;width:274px;height:70px;background:var(--orange);padding:12px 0 0 18px;color:#fff}
  .name-bar .person{font-weight:700;font-size:24px;line-height:1.05;text-transform:uppercase}
  .name-bar .role{font-size:14px}
  .details{position:absolute;left:70px;top:70px;width:274px;height:330px;background:var(--panel-mid)}
  .detail-row{height:66px;display:flex;flex-direction:column;justify-content:center;padding-left:18px;color:var(--text);font-size:14px;line-height:1.3;border-bottom:2px solid var(--rule);margin-right:24px}
  .detail-row--address{height:120px;border-bottom:none;font-size:14px}
  .icon-col{position:absolute;left:0;top:40px;width:70px}
  .icon{display:flex;justify-content:center;align-items:center;height:66px;border-bottom:2px solid var(--orange);margin:0 10px}
  .icon:last-child{border-bottom:none}
  .icon svg{width:30px;height:30px;fill:var(--orange)}

  .card--back .brand-strip{top:110px;height:96px;flex-direction:column;align-items:flex-start;justify-content:center}
  .web-line{font-size:15px;margin-top:4px;color:var(--orange)}
  .web-line .mid{color:var(--teal)}
</style>
</head>
<body>
  <section class="card card--front">
    <div class="brand-strip"><span class="brand-name">BRIVAN CASES</span></div>
    <div class="contact-panel">
      <div class="name-bar">
        <div class="person">Mark Dunsley</div>
        <div class="role">Company owner</div>
      </div>
      <div class="icon-col">
        <div class="icon"><svg viewBox="0 0 24 24"><circle cx="12" cy="8" r="5"/><path d="M3 22c0-5 4-8 9-8s9 3 9 8z"/></svg></div>
        <div class="icon"><svg viewBox="0 0 24 24"><path d="M6 2l4 4-2 3c1 3 4 6 7 7l3-2 4 4-3 4C10 21 3 14 2 5z"/></svg></div>
        <div class="icon"><svg viewBox="0 0 24 24"><path d="M2 5h20v14H2z M3 6l9 7 9-7" fill="none" stroke="#eb9d35" stroke-width="2"/></svg></div>
        <div class="icon"><svg viewBox="0 0 24 24" fill="none" stroke="#eb9d35" stroke-width="1.8" style="fill:none"><circle cx="12" cy="12" r="9.5"/><ellipse cx="12" cy="12" rx="4.5" ry="9.5"/><path d="M2.5 12h19M4 7h16M4 17h16"/></svg></div>
        <div class="icon"><svg viewBox="0 0 24 24"><path d="M12 3l10 9h-3v9h-5v-6h-4v6H5v-9H2z"/></svg></div>
      </div>
      <div class="details">
        <div class="detail-row"><span>027 . 512 . 4068</span><span>09 . 528 . 3916</span></div>
        <div class="detail-row">sales@brivancases.co.nz</div>
        <div class="detail-row">www.brivancases.co.nz</div>
        <div class="detail-row detail-row--address">
          <span>3/17 Harlow Street</span>
          <span>Pinecrest Flats, Auckland, 0614</span>
          <span>PO Box 204377, Fernside</span>
          <span>Auckland 0731</span>
        </div>
      </div>
    </div>
  </section>

  <section class="card card--back">
    <div class="brand-strip">
      <span class="brand-name">BRIVAN CASES</span>
      <span class="web-line">www.<span class="mid">brivancases</span>.co.nz</span>
    </div>
  </section>
</body>
</html>
```